Business card for a "family office" company

Please provide professional looking business card designs, incorporating the attached logo and below details. Harrowmere Holdings Pty Ltd is a family office / financial investment company. We are looking for a modern, professional and contemporary card design.

Industry/Entity Type

Finance

Contact Information for Business Card

Name: Dean Mollick
Title: Director
Company: Harrowmere Holdings Pty Ltd
Email: harrowdean@quillnet.example
Mobile: 0462 735 418
Address: 4/312 Barnaby Parade, Cottesloe WA 6011, Australia

Requirements
Must have
• All details above and the logo. logo only on back side. incorporate colours of logo
Nice to have
• up to you
Should not have
• ?

```html
<!DOCTYPE html>
<html lang="en">
<head>
<meta charset="utf-8">
<title>Harrowmere Holdings – Business Card</title>
<link rel="stylesheet" href="https://fonts.googleapis.com/css2?family=Montserrat:wght@400;500;600&display=swap">
<style>
  :root {
    --navy: #1e1f5c;
    --white: #ffffff;
    --grey-text: #6b6b72;
    --backdrop: #3a3a3d;
    --rule: #3b3c72;
  }
  * { margin: 0; padding: 0; box-sizing: border-box; }
  html, body { width: 1200px; height: 864px; overflow: hidden; }
  body {
    background: var(--backdrop);
    font-family: "Montserrat", Arial, sans-serif;
    position: relative;
  }
  .card {
    position: absolute;
    top: 273px;
    width: 520px;
    height: 318px;
    border-radius: 3px;
    box-shadow: 0 10px 30px rgba(0,0,0,0.35);
  }
  .card-back { left: 50px; background: var(--navy); display: flex; align-items: center; justify-content: center; }
  .card-front { left: 630px; background: var(--white); color: var(--navy); }

  .brand-mark { display: flex; align-items: center; gap: 10px; font-weight: 600; letter-spacing: 0.06em; }
  .brand-mark .mark-square { width: 16px; height: 16px; background: currentColor; }
  .card-back .brand-mark { color: var(--white); font-size: 24px; }

  .card-front .brand-mark {
    position: absolute; top: 52px; right: 40px;
    font-size: 18px; color: var(--navy);
  }
  .card-front .brand-mark .mark-square { width: 13px; height: 13px; }

  .holder { position: absolute; left: 40px; top: 168px; }
  .holder-name { font-size: 20px; font-weight: 600; color: var(--navy); }
  .holder-title { font-size: 14px; color: var(--grey-text); margin-top: 2px; }

  .address {
    position: absolute; right: 40px; top: 172px;
    text-align: right; font-size: 13px; line-height: 1.5; color: var(--grey-text);
  }

  .divider {
    position: absolute; left: 40px; right: 40px; top: 218px;
    height: 1px; background: var(--rule);
  }

  .contact { position: absolute; left: 40px; top: 234px; list-style: none; font-size: 14px; color: var(--grey-text); }
  .contact li { display: flex; align-items: center; gap: 9px; line-height: 24px; }
  .contact svg { width: 13px; height: 13px; fill: var(--navy); flex: none; }
</style>
</head>
<body>
  <section class="card card-back" aria-label="Card back">
    <div class="brand-mark"><span class="mark-square"></span>HARROWMERE HOLDINGS</div>
  </section>

  <section class="card card-front" aria-label="Card front">
    <div class="brand-mark"><span class="mark-square"></span>HARROWMERE HOLDINGS</div>

    <div class="holder">
      <p class="holder-name">Dean Mollick</p>
      <p class="holder-title">Director</p>
    </div>

    <p class="address">4/312 Barnaby Parade<br>Cottesloe WA 6011, Australia</p>

    <div class="divider"></div>

    <ul class="contact">
      <li>
        <svg viewBox="0 0 24 24" aria-hidden="true"><path d="M6.6 10.8a15.1 15.1 0 0 0 6.6 6.6l2.2-2.2a1 1 0 0 1 1-.25 11.4 11.4 0 0 0 3.6.57 1 1 0 0 1 1 1V20a1 1 0 0 1-1 1A17 17 0 0 1 3 4a1 1 0 0 1 1-1h3.5a1 1 0 0 1 1 1c0 1.25.2 2.45.57 3.57a1 1 0 0 1-.25 1z"/></svg>
        0462 735 418
      </li>
      <li>
        <svg viewBox="0 0 24 24" aria-hidden="true"><path d="M2 5h20v14H2z M3.5 6.5 12 13l8.5-6.5" fill="var(--navy)"/><path d="M3 6l9 7 9-7" fill="none" stroke="#fff" stroke-width="1.6"/></svg>
        harrowdean@quillnet.example
      </li>
    </ul>
  </section>
</body>
</html>
```